email presentation and marketing

we need a email to be used to present our company and services to potential customer. it needs to contain our logo, address, details about our company, photos and a well described text about our work .
I will send a web site from one of the company we are targeting.
The e mail must be sober, elegant, persuasive. The client needs to have the feeling it is dealing to a big company.
See below one of out potential clients
http://qorbelresidences.com/

Target Market(s)

High end custom homes

Industry/Entity Type

Painting And Decorating

Font styles to use
Serif
Sans Serif

Requirements
Must have
• Our name, location, portfolio (need to send some pics), web site http://kd-brushworks.com.
• Need to develop a email to present our company to potential clients.
Nice to have
• clients reviews.
• we are listed on nest rater. https://nestrater.net/firms/5813064-kd-bespoke?service_area=7640153
Should not have
• not colorful

```html
<!DOCTYPE html>
<html lang="en">
<head>
<meta charset="utf-8">
<title>KD Brushworks – Introduction</title>
<link href="https://fonts.googleapis.com/css2?family=Lato:wght@400;700&family=Roboto:ital,wght@0,400;0,500;0,700;1,400&display=swap" rel="stylesheet">
<style>
:root{
  --paper:#efefef;
  --slate:#353a45;
  --slate-deep:#2b2f37;
  --gold:#e0c10c;
  --ink:#1d1d1d;
  --muted:#6b6b6b;
  --white:#ffffff;
}
*{margin:0;padding:0;box-sizing:border-box}
html,body{width:1200px;height:3098px;overflow:hidden;background:var(--paper)}
body{position:relative;font-family:"Roboto",Arial,sans-serif;color:var(--ink)}
.abs{position:absolute}

/* header */
.header{left:0;top:0;width:1200px;height:190px;background:var(--paper)}
.header-phone{left:330px;top:80px;width:176px;text-align:right;font-size:20px}
.header-mail{left:230px;top:112px;width:276px;text-align:right;font-size:12px}
.brand{font-family:"Roboto",Arial,sans-serif;font-weight:700;color:var(--gold);letter-spacing:1px;white-space:nowrap}
.header-brand{left:540px;top:78px;width:180px;text-align:center;font-size:22px}
.header-address{left:756px;top:80px;font-size:20px}
.header-postal{left:756px;top:108px;font-size:13px}

/* hero */
.hero-band{left:0;top:190px;width:1200px;height:1210px;background:var(--slate)}
.hero-side{left:0;top:280px;width:60px;height:525px;background:linear-gradient(90deg,#8a8680,#d9d6d1)}
.hero-photo{left:66px;top:235px;width:1126px;height:641px;background:linear-gradient(180deg,#e6eef5 0%,#b9b2a6 45%,#6f675c 70%,#5e6b49 88%,#7b7a72 100%)}
.tagline{left:256px;top:822px;width:750px;height:78px;background:var(--gold);display:flex;align-items:center;justify-content:center;font-weight:700;font-size:28px;color:var(--ink)}
.intro-card{left:256px;top:900px;width:750px;height:463px;background:var(--white);border-radius:0 0 16px 16px}
.intro-text{left:29px;top:50px;width:430px;font-family:"Lato",Arial,sans-serif;font-size:19.5px;line-height:32px;color:var(--ink)}
.intro-divider{left:500px;top:20px;width:1px;height:298px;background:#d6d6d6}
.services{left:514px;top:56px;list-style:none;font-weight:700;font-size:17.5px;line-height:24px;text-transform:uppercase}
.services li{position:absolute;left:0;width:200px}
.btn-quote{width:312px;height:46px;border-radius:23px;background:var(--gold);display:flex;align-items:center;justify-content:center;font-size:24px;font-weight:500;color:var(--ink)}

/* testimonials */
.section-title{left:0;width:1200px;text-align:center;font-size:30px;font-weight:500}
.review{width:370px;text-align:center}
.review-avatar{display:block;margin:0 auto}
.review-name{margin-top:18px;font-style:italic;font-size:20px;color:var(--muted)}
.review-job{margin-top:30px;font-size:17px;color:var(--muted)}
.review-quote{margin-top:30px;font-style:italic;font-size:15.5px;line-height:22px;color:var(--muted)}
.photo{background:linear-gradient(160deg,#ececea,#bdb8b1 60%,#8d857b)}
.works-bar{left:256px;top:2160px;width:750px;height:72px;background:var(--slate);display:flex;align-items:center;justify-content:center;color:var(--white);font-size:30px;font-weight:500}
.thumb{top:2257px;width:142px;height:236px;background:linear-gradient(170deg,#eeeeec,#b9b4ac 55%,#4a3f37)}

/* footer */
.footer{left:0;top:2618px;width:1200px;height:407px;background:var(--slate)}
.footer-brand{left:0;top:2690px;width:1200px;text-align:center;font-size:30px}
.footer-info{left:0;top:2778px;width:1200px;text-align:center;color:var(--white);font-size:20px;line-height:25.5px}
.social{left:480px;top:2950px}
.legal{left:0;top:3025px;width:1200px;height:73px;background:var(--slate-deep);display:flex;align-items:center;justify-content:center;color:var(--white);font-size:20px}
</style>
</head>
<body>

<header class="abs header">
  <div class="abs header-phone">416 555 0182</div>
  <div class="abs header-mail">info@brushworkspro.com</div>
  <div class="abs header-brand brand">KD BRUSHWORKS</div>
  <div class="abs header-address">214 Linden Crest Rd, Unit C3</div>
  <div class="abs header-postal">M4R 2K7</div>
</header>

<section class="abs hero-band"></section>
<div class="abs hero-side" role="img" aria-label="Edge of a neighbouring slide photo"></div>
<div class="abs hero-photo" role="img" aria-label="Large stone custom home with dark roof and lit entrance at dusk"></div>
<div class="abs tagline">KD BRUSHWORKS – WE ARE ALWAYS READY TO SERVE</div>

<article class="abs intro-card">
  <p class="abs intro-text">K.D Brushworks is a Toronto based company that provides customised home painting, commercial and industrial painting services to Greater Toronto and metropolitan cities. We use modern equipment and superior brand materials to deliver a high-quality work which makes us nothing less then proud.</p>
  <div class="abs intro-divider"></div>
  <ul class="abs services">
    <li style="top:0">- Wallpaper<br>&nbsp;&nbsp;Installation</li>
    <li style="top:80px">- Spray Finish</li>
    <li style="top:136px">- Drywall Repairs</li>
    <li style="top:192px">- Staircase Finish</li>
  </ul>
  <div class="abs btn-quote" style="left:219px;top:345px">GET A QUOTE</div>
</article>

<h2 class="abs section-title" style="top:1430px">CLIENT TESTIMONIALS</h2>

<div class="abs review" style="left:259px;top:1500px">
  <svg class="review-avatar" width="76" height="76" viewBox="0 0 76 76" aria-hidden="true">
    <circle cx="38" cy="38" r="37" fill="#111"/>
    <circle cx="38" cy="29" r="12" fill="#fff"/>
    <path d="M16 60c4-12 13-16 22-16s18 4 22 16a31 31 0 0 1-44 0z" fill="#fff"/>
  </svg>
  <div class="review-name">DARIO</div>
  <div class="review-job">Paint Of &nbsp;New Homes and Renovations</div>
  <p class="review-quote">Marco and his staff are reliable, provide great quality and service. myself and my clients are extremely satisfied with his work.</p>
</div>

<div class="abs review" style="left:635px;top:1500px">
  <svg class="review-avatar" width="76" height="76" viewBox="0 0 76 76" aria-hidden="true">
    <circle cx="38" cy="38" r="37" fill="#111"/>
    <circle cx="38" cy="29" r="12" fill="#fff"/>
    <path d="M16 60c4-12 13-16 22-16s18 4 22 16a31 31 0 0 1-44 0z" fill="#fff"/>
  </svg>
  <div class="review-name">Norvale Build</div>
  <div class="review-job">Painting Of New Home</div>
  <p class="review-quote">Contractor was hired to paint New home. Staff was friendly, courteous, helpful, clean, proactive, reliable.</p>
</div>

<div class="abs photo" style="left:270px;top:1790px;width:345px;height:343px" role="img" aria-label="Curved wooden staircase with iron railing during finishing work"></div>
<div class="abs photo" style="left:646px;top:1790px;width:345px;height:343px" role="img" aria-label="Freshly painted living room with stone fireplace and tall black windows"></div>

<div class="abs works-bar">OUR WORKS</div>
<div class="abs thumb" style="left:279px" role="img" aria-label="White painted room with bay window"></div>
<div class="abs thumb" style="left:467px" role="img" aria-label="Dark stained curved staircase"></div>
<div class="abs thumb" style="left:655px" role="img" aria-label="Long hallway with dark hardwood floor"></div>
<div class="abs thumb" style="left:843px" role="img" aria-label="Stone fireplace with built-in shelving"></div>

<div class="abs btn-quote" style="left:475px;top:2540px">GET A QUOTE</div>

<footer class="abs footer"></footer>
<div class="abs footer-brand brand">KD BRUSHWORKS</div>
<div class="abs footer-info">
  KD Brushworks<br>
  Contact: Marco Reis<br>
  416 555 0182|kdbrushworks.office@mail.com<br>
  kd-brushworks.com
</div>
<svg class="abs social" width="304" height="50" viewBox="0 0 304 50" aria-label="Social profiles">
  <g fill="none" stroke="#d8d8d8" stroke-width="2">
    <circle cx="24" cy="25" r="23"/>
    <circle cx="88" cy="25" r="23"/>
    <circle cx="152" cy="25" r="23"/>
    <circle cx="216" cy="25" r="23"/>
    <circle cx="280" cy="25" r="23"/>
  </g>
</svg>
<div class="abs legal">KD Brushworks © All rights reserved</div>

</body>
</html>
```